Professional "Torvinex" Auction Website with Customer Login Backend Module

Need an "Torvinex" Website with 4 major listing options.
- AUCTION
Seller can list their items on the site as an auction with a small listing fee. Seller has to create an account in order to be able to create or edit a listing. Seller must be able to have a reserve price.
- SELLING
Sellers can list their items with a small listing fee. Imortant is, that Sellers has a back end module, (like lotvane) where they can log in and create or make changes to existing listings.
- BUYING
Buyers can search items either by part number in a search bar, or scroll through categories and subcategories to find the respective part.
- WANTED
Customers should be able to create a “Wanted” listing for items of interest.

In all four cases, customers (Buyers/Seller) must create an account to either place a bid, buy now, create a “wanted” listing or create/edit their own for sale/auction listing. NO login is required to search the website or browse through categories and to see listings. The website should be “Lotvane like” with login module, payment, coinrill connection, etc and easy to navigate. A design example is https://www.skylotra-hub.com/ . I’m open for all ideas.

Target Market(s)

Aviation Industry
Helicopter Industry

Industry/Entity Type

Aviation

Number of Pages Required

5+ page

Font styles to use
Serif
Sans Serif

Colors
85acd3
3176b5
9d9d9d
d3d3d3

Requirements
Must have
• Our company is called Torvinex.com, LLC and is specialized in Torvinex listings. The website must have 4 major options: Auction, Sell, Buy, and Wanted listings. The Buyer/Seller must create an account in order to bid, buy or sell an item. No login is required if someone just wants to browse the website to look for pricing and parts. Once they decide to purchase, they have to login or create an account. The same counts for the seller. Seller must create an account to list a "For Sale", "Auction" or "Wanted" Listing. Each listing requires a small listing fee, which will be charged by us and should be paid via CoinRill. CoinRill should be interfaced as a preferred payment method. Other payment options are available as well. The website idea is very similar to Lotvane. Same style listings as Lotvane and other auction pages. A good design idea is https://www.skylotra-hub.com/ to get a better understanding. The website must be easy to navigate and modern looking with a professional color scheme. The logo is attached. I would like to keep the website in a similar color scheme as the logo design.
• There should be two main Categories on the main page to select from:
• - Helicopter Listings
• - Airplane Listings
• The 1st "Sub-Category" once you click on either one of the top category, will be "Aircraft Make".
• The 2nd "Sub-Category" will be "Aircraft Model".
• The 3rd "Sub-Category" will be "Parts" for that specific aircraft.
• Also there should be a CoinRill interface, if a buyer wants to purchase an item, so they can use their credit card or request wire information from the seller after closing.
• It also has to include an option when a seller lists an item, they will be required to make a payment to us for listing on our website. For example $1.99 for a listing value up to $100. A listing fee for a sale value of up to $1,000 will be $4.99, and so on. Listing fee for up to $10,000 will be $14.99. Listing fee for up to $100.000 will be $49.99. This system is very similar to the Lotvane platform.
Nice to have
• It would be nice to have a easy to maintain back-end module which can easily be manged by our personnel.
Should not have
• The page should not look childish with random colors. A professional appearance and easy to navigate is a must.

```html
<!DOCTYPE html>
<html lang="en">
<head>
<meta charset="utf-8">
<title>Torvinex – Bleed Air Flow Control Valve</title>
<link href="https://fonts.googleapis.com/css2?family=Montserrat:wght@400;500;600&family=Open+Sans:wght@400&display=swap" rel="stylesheet">
<style>
:root{
  --header:#6798c9;
  --primary:#3176b5;
  --grey:#9d9d9d;
  --light:#d3d3d3;
  --text:#555;
  --panel:#e8f4fd;
  --footer:#06476f;
  --star:#f5c518;
}
*{margin:0;padding:0;box-sizing:border-box}
html,body{width:1200px;height:1057px;overflow:hidden;background:#fff}
body{position:relative;font-family:'Montserrat',sans-serif;color:var(--text)}
.abs{position:absolute}

.site-header{position:absolute;left:0;top:0;width:1200px;height:141px;background:var(--header)}
.brand{position:absolute;left:96px;top:26px;display:flex;align-items:center;gap:10px}
.brand-mark{width:84px;height:84px;border-radius:50%;background:#fff}
.brand-name{color:#fff;font-size:18px;font-weight:600}
.main-nav{position:absolute;top:56px;left:575px;display:flex;gap:34px;font-size:17px;color:#fff}
.signup{position:absolute;left:886px;top:45px;width:102px;height:49px;background:var(--primary);color:#fff;border-radius:5px;font-size:19px;display:flex;align-items:center;justify-content:center}
.cart-icon{position:absolute;left:1016px;top:54px}
.heart-icon{position:absolute;left:1072px;top:57px}

.breadcrumb{position:absolute;left:96px;top:180px;font-size:17px;color:var(--primary);display:flex;gap:9px}

.product-photo{position:absolute;left:99px;top:235px;width:460px;height:224px;background:radial-gradient(ellipse at 55% 55%,#c9b98f 0%,#a8a690 35%,#ecebe6 72%,#fff 100%);box-shadow:0 1px 4px rgba(0,0,0,.25)}
.thumbs{position:absolute;left:99px;top:478px;display:flex;gap:11px}
.thumb{width:107px;height:89px;border:1px solid var(--light);padding:4px;background:#fff}
.thumb span{display:block;width:100%;height:100%;background:radial-gradient(ellipse at 50% 55%,#c4b68c 0%,#aaa894 40%,#efeee9 80%)}

.product-title{position:absolute;left:595px;top:240px;font-size:21px;font-weight:500;color:#444}
.rating{position:absolute;left:595px;top:288px;display:flex;gap:5px}
.price-row{position:absolute;left:596px;display:flex;align-items:baseline;font-size:19px;color:var(--grey)}
.price-row .value{position:absolute;left:153px;font-size:26px;color:var(--primary);white-space:nowrap}
.bid-input{position:absolute;left:865px;top:428px;width:238px;height:48px;border-radius:5px;background:#eee;overflow:hidden;display:flex}
.bid-input .field{flex:1;font-size:22px;color:#ccc;padding:12px 0 0 14px;border-left:1px solid #bbb;margin:10px 0 10px 10px;padding-top:2px;padding-left:6px}
.bid-input .btn{width:105px;background:var(--primary);color:#fff;font-size:19px;display:flex;align-items:center;justify-content:center}
.action{position:absolute;top:522px;display:flex;align-items:center;gap:12px;font-size:17px;color:var(--grey)}

.tabs{position:absolute;left:99px;top:607px;width:1004px;height:53px;display:flex;background:linear-gradient(#eef7fd,#cfe6f7)}
.tab{display:flex;align-items:center;justify-content:center;font-size:19px;color:#888;border-right:1px solid #b9cfe0}
.tab.active{background:var(--primary);color:#fff}
.tab-panel{position:absolute;left:99px;top:660px;width:1004px;height:152px;background:var(--panel);box-shadow:0 1px 3px rgba(0,0,0,.12);padding:20px 0 0 20px;font-family:'Open Sans',sans-serif;font-size:16px;line-height:27px;color:#666}
.tab-panel p{width:800px;text-indent:30px}

.site-footer{position:absolute;left:0;top:881px;width:1200px;height:176px;background:var(--footer);color:#fff;font-size:14px}
.footer-col{position:absolute;top:28px;display:flex;flex-direction:column;gap:14px}
.footer-col h4{font-size:15px;font-weight:600;margin-bottom:3px}
.footer-contact{position:absolute;right:98px;top:0;height:176px}
.footer-contact span{position:absolute;white-space:nowrap}
</style>
</head>
<body>

<header class="site-header">
  <div class="brand"><div class="brand-mark"></div><span class="brand-name">Torvinex</span></div>
  <nav class="main-nav"><span>Sell</span><span>Buy</span><span>Contact</span><span>Login</span></nav>
  <div class="signup">Sign up</div>
  <svg class="cart-icon" width="30" height="30" viewBox="0 0 30 30" fill="none" stroke="#fff" stroke-width="2.6" stroke-linecap="round" stroke-linejoin="round">
    <path d="M2 8h4l3 12h13l3-9H8"/><circle cx="11" cy="25" r="2" fill="#fff"/><circle cx="20" cy="25" r="2" fill="#fff"/>
    <circle cx="24" cy="4" r="4" fill="var(--primary)" stroke="none"/><text x="24" y="6.5" font-size="7" fill="#fff" stroke="none" text-anchor="middle" font-family="Montserrat">1</text>
  </svg>
  <svg class="heart-icon" width="26" height="24" viewBox="0 0 26 24" fill="none" stroke="#fff" stroke-width="2.6"><path d="M13 21 3.5 11.5a5.5 5.5 0 0 1 9.5-6 5.5 5.5 0 0 1 9.5 6z"/></svg>
</header>

<nav class="breadcrumb"><span>Home</span><span>&gt;</span><span>Categorie</span><span>&gt;</span><span>Aircraft Parts</span><span>&gt;</span><span>Pneumatic - ATA 36</span><span>&gt;</span><span>Bleed air flow valve</span></nav>

<div class="product-photo" role="img" aria-label="Photo of a bleed air flow control valve assembly"></div>
<div class="thumbs">
  <div class="thumb"><span role="img" aria-label="Valve view 1"></span></div>
  <div class="thumb"><span role="img" aria-label="Valve view 2"></span></div>
  <div class="thumb"><span role="img" aria-label="Valve view 3"></span></div>
  <div class="thumb"><span role="img" aria-label="Valve view 4"></span></div>
</div>

<h1 class="product-title">Bleed Air Flow Control Valve</h1>
<div class="rating">
  <svg width="110" height="16" viewBox="0 0 110 16">
    <defs><path id="star" d="M8 0l2.4 5 5.4.6-4 3.7 1.1 5.4L8 12 3.1 14.7l1.1-5.4-4-3.7L5.6 5z"/></defs>
    <use href="#star" fill="var(--star)"/><use href="#star" x="22" fill="var(--star)"/><use href="#star" x="44" fill="var(--star)"/><use href="#star" x="66" fill="var(--star)"/><use href="#star" x="88" fill="#ccc"/>
  </svg>
</div>

<div class="price-row" style="top:342px"><span>Current Price :</span><span class="value">$1076.25</span></div>
<div class="price-row" style="top:393px"><span>Minimum Bid :</span><span class="value">$1077</span></div>
<div class="price-row" style="top:449px"><span>Enter your Maximum Bid</span></div>
<div class="bid-input"><span class="field">$1077</span><span class="btn">Place Bid</span></div>

<div class="action" style="left:596px">
  <svg width="28" height="26" viewBox="0 0 28 26" fill="none" stroke="var(--primary)" stroke-width="2.4" stroke-linecap="round" stroke-linejoin="round"><path d="M2 3h4l3 12h13l3-9H7"/><circle cx="10" cy="21" r="2"/><circle cx="20" cy="21" r="2"/></svg>
  <span>Add to my Cart</span>
</div>
<div class="action" style="left:818px">
  <svg width="26" height="24" viewBox="0 0 26 24" fill="none" stroke="var(--primary)" stroke-width="2.4"><path d="M13 21 3.5 11.5a5.5 5.5 0 0 1 9.5-6 5.5 5.5 0 0 1 9.5 6z"/></svg>
  <span>Add to my Wanted List</span>
</div>

<div class="tabs">
  <div class="tab active" style="width:303px">Product Description</div>
  <div class="tab" style="width:180px">Features</div>
  <div class="tab" style="width:260px">Specification</div>
  <div class="tab" style="width:261px;border-right:0">Customer Review</div>
</div>
<section class="tab-panel">
  <p>Lorem ipsum dolor sit amet, consectetur adipiscing elit. Maecenas a luctus lorem. Vestibulum ele-mentum accumsan orci id ullamcorper. Ut dui erat.Lorem ipsum dolor sit amet, consectetur adipiscing elit. Maecenas a luctus lorem. Vestibulum elementum accumsan orci id ullamcorper. Ut dui erat, Ut dui erat.Lorem ipsum dolor sit amet, consectetur adipiscing</p>
</section>

<footer class="site-footer">
  <div class="footer-col" style="left:113px"><h4>THE COMPANY</h4><span>ABOUT US</span><span>WHAT WE OFFER</span><span>TERMS OF SERVICE</span></div>
  <div class="footer-col" style="left:412px"><h4>LET US HELP YOU</h4><span>YOUR ORDERS</span><span>SUPPORT</span><span>FAQ</span></div>
  <div class="footer-contact">
    <span style="left:-251px;top:31px">CALL US : (555-014-2290)</span>
    <span style="left:-251px;top:77px">MAIL@TORVINEX.COM</span>
    <span style="right:0;top:123px">© TORVINEX. ALL RIGHTS RESERVED 2018</span>
  </div>
</footer>

</body>
</html>
```